Cannabis Company needs a packaging design for a 4x6 pouch

We need a design for a new cannabis company. Included is the logo in red. The logo color can change. Whatever color looks best with the design is what we'll use. The design can't include any cartoon characters or anything that may appeal to children. We have multiple products that are similar that will be using the same design. The pouch will contain 10 pyramid shaped gummies. The look we're going for is modern, simple, but eye catching. I included a handful of photos of packaging we like if that helps.

```html
<!DOCTYPE html>
<html lang="en">
<head>
<meta charset="utf-8">
<title>Verdane Delta-8 THC Gummies – Pouch Front</title>
<link href="https://fonts.googleapis.com/css2?family=Bebas+Neue&display=swap" rel="stylesheet">
<style>
  :root {
    --backdrop: #ebebeb;
    --pattern-gold: #e8a632;
    --pattern-rust: #b04a3a;
    --pattern-maroon: #7d3026;
    --panel-light: #f6bd3f;
    --panel-mid: #eca42c;
    --panel-deep: #d9891c;
    --label-text: #fffaf0;
    --brand-ink: #161412;
  }
  * { margin: 0; padding: 0; box-sizing: border-box; }
  html, body {
    width: 1200px;
    height: 1200px;
    overflow: hidden;
    background: var(--backdrop);
  }
  .canvas {
    position: relative;
    width: 1200px;
    height: 1200px;
    background: var(--backdrop);
  }
  .pouch {
    position: absolute;
    left: 260px;
    top: 60px;
    width: 680px;
    height: 1080px;
    border-radius: 22px 22px 14px 14px;
    overflow: hidden;
    background: linear-gradient(135deg,
      var(--pattern-gold) 0%,
      var(--pattern-rust) 45%,
      var(--pattern-maroon) 70%,
      var(--pattern-gold) 100%);
  }
  .label-panel {
    position: absolute;
    left: 93px;
    top: 218px;
    width: 497px;
    height: 734px;
    background: linear-gradient(160deg,
      var(--panel-light) 0%,
      var(--panel-mid) 45%,
      var(--panel-deep) 100%);
    font-family: "Bebas Neue", sans-serif;
    color: var(--label-text);
    text-align: center;
  }
  .claims {
    position: absolute;
    top: 46px;
    left: 0;
    right: 0;
    font-size: 34px;
    letter-spacing: 1.5px;
  }
  .brand {
    position: absolute;
    top: 250px;
    left: 0;
    right: 0;
    display: flex;
    align-items: center;
    justify-content: center;
    gap: 16px;
    color: var(--brand-ink);
  }
  .brand-square {
    width: 22px;
    height: 22px;
    background: var(--brand-ink);
  }
  .brand-name {
    font-size: 86px;
    letter-spacing: 3px;
    line-height: 1;
  }
  .product-name {
    position: absolute;
    top: 435px;
    left: 0;
    right: 0;
    font-size: 68px;
    line-height: 84px;
    letter-spacing: 4px;
  }
  .pack-details {
    position: absolute;
    top: 655px;
    left: 0;
    right: 0;
    font-size: 24px;
    line-height: 28px;
    letter-spacing: 1px;
  }
</style>
</head>
<body>
  <main class="canvas">
    <section class="pouch" role="img" aria-label="Chevron zigzag pattern in gold, rust and maroon covering the pouch">
      <div class="label-panel">
        <p class="claims">Gluten Free - Non GMO - Fat Free</p>
        <div class="brand">
          <span class="brand-square"></span>
          <span class="brand-name">Verdane</span>
        </div>
        <h1 class="product-name">Delta - 8 THC<br>Gummies</h1>
        <p class="pack-details">10 Gummies<br>25mg Delta 8 per Gummy</p>
      </div>
    </section>
  </main>
</body>
</html>
```